New Webpage for High Class Expert Witness Services Company

We are looking for a minimalist design for a webpage that just has our logo and an entry form offer to connect with one of our Liaisons.
The entry form should just ask for Name, Email, Contact Info and Description of Project.

Company Name is: The Marlow Crest Advisory Services

Number of Pages Required

1 page

```html
<!DOCTYPE html>
<html lang="en">
<head>
<meta charset="UTF-8">
<title>The Marlow Crest Advisory Services</title>
<link rel="stylesheet" href="https://fonts.googleapis.com/css2?family=Cinzel:wght@500;600;700&family=Poppins:wght@400;600&display=swap">
<style>
  :root {
    --ink: #111111;
    --ink-soft: #3a3a3a;
    --panel-light: #fbfbfb;
    --panel-mid: #e6e6e6;
    --card: #ffffff;
    --field-border: #cfcfcf;
    --placeholder: #8a8a8a;
    --button: #232323;
    --button-text: #ffffff;
    --photo-light: #eef0ef;
    --photo-mid: #c9ccca;
    --photo-dark: #8e918f;
  }
  * { box-sizing: border-box; margin: 0; padding: 0; }
  html, body { width: 1200px; height: 675px; overflow: hidden; }
  body { position: relative; font-family: "Poppins", sans-serif; color: var(--ink); }

  .intro-panel {
    position: absolute; left: 0; top: 0; width: 597px; height: 675px;
    background: linear-gradient(160deg, var(--panel-light) 0%, #f1f1f1 45%, var(--panel-mid) 100%);
  }

  .brand { position: absolute; left: 122px; top: 27px; height: 48px; display: flex; align-items: center; gap: 9px; }
  .brand-mark { width: 30px; height: 30px; background: var(--ink); }
  .brand-text {
    height: 48px; border-left: 1px solid var(--ink-soft); padding-left: 7px;
    display: flex; flex-direction: column; justify-content: center; align-items: center;
  }
  .brand-name {
    font-family: "Cinzel", serif; font-weight: 600; font-size: 23px;
    line-height: 1; color: var(--ink); letter-spacing: 0.3px; white-space: nowrap;
  }
  .brand-subline {
    font-family: "Cinzel", serif; font-weight: 500; font-size: 13.5px;
    line-height: 1; letter-spacing: 2px; color: var(--ink); margin-top: 3px; white-space: nowrap;
  }
  .brand-tagline {
    font-family: "Cinzel", serif; font-weight: 500; font-size: 7.4px;
    line-height: 1; letter-spacing: 1.9px; color: var(--ink-soft); margin-top: 4px; white-space: nowrap;
  }

  .headline {
    position: absolute; left: 122px; top: 125px; height: 139px;
    border-left: 1px solid var(--ink); padding-left: 22px;
    display: flex; align-items: center;
  }
  .headline h1 {
    font-family: "Cinzel", serif; font-weight: 700; font-size: 36px;
    line-height: 49px; letter-spacing: 0.8px; width: 380px;
  }

  .contact-card {
    position: absolute; left: 122px; top: 286px; width: 394px; height: 334px;
    background: var(--card);
  }
  .contact-card h2 {
    position: absolute; left: 22px; top: 17px;
    font-family: "Cinzel", serif; font-weight: 600; font-size: 18.6px;
    letter-spacing: 0.6px; white-space: nowrap;
  }
  .field {
    position: absolute; left: 21px; width: 349px; height: 36px;
    border: 1px solid var(--field-border); background: var(--card);
    font-family: "Poppins", sans-serif; font-size: 10.5px; color: var(--ink);
    padding: 0 12px; outline: none;
  }
  .field::placeholder { color: var(--placeholder); }
  .field-name { top: 55px; }
  .field-email { top: 98px; }
  .field-phone { top: 141px; }
  .field-project { top: 184px; height: 75px; padding-top: 10px; resize: none; }
  .submit {
    position: absolute; left: 20px; top: 273px; width: 350px; height: 39px;
    background: var(--button); color: var(--button-text); border: none;
    font-family: "Poppins", sans-serif; font-weight: 600; font-size: 11px;
    letter-spacing: 0.3px;
  }

  .legal {
    position: absolute; left: 122px; top: 650px;
    font-size: 9.4px; color: var(--ink); white-space: nowrap;
  }

  .hero-visual {
    position: absolute; left: 597px; top: 0; width: 603px; height: 675px;
    border-left: 2px solid #b9bbba;
    background: linear-gradient(90deg, var(--photo-light) 0%, #f7f8f7 25%, var(--photo-mid) 55%, var(--photo-dark) 78%, var(--photo-mid) 88%, #d7d8d6 100%);
    overflow: hidden;
  }
  .hero-word {
    position: absolute; right: -8px; top: 0;
    writing-mode: vertical-rl;
    font-family: "Cinzel", serif; font-weight: 500; font-size: 92px;
    letter-spacing: 4px; color: rgba(0, 0, 0, 0.06); line-height: 1;
  }
</style>
</head>
<body>
  <section class="intro-panel">
    <div class="brand">
      <div class="brand-mark"></div>
      <div class="brand-text">
        <div class="brand-name">MARLOW CREST</div>
        <div class="brand-subline">— ADVISORY SERVICES —</div>
        <div class="brand-tagline">DISCREET EXPERT WITNESS COORDINATION</div>
      </div>
    </div>

    <div class="headline">
      <h1>THE MARLOW CREST ADVISORY SERVICES</h1>
    </div>

    <form class="contact-card">
      <h2>CONTACT OUR DEFENSE LIAISONS</h2>
      <input class="field field-name" type="text" placeholder="Name*">
      <input class="field field-email" type="email" placeholder="Email*">
      <input class="field field-phone" type="tel" placeholder="Phone*">
      <textarea class="field field-project" placeholder="Project Description*"></textarea>
      <button class="submit" type="button">SUBMIT</button>
    </form>

    <p class="legal">© The Marlow Crest Advisory Services | All inquiries are handled with strict confidentiality.</p>
  </section>

  <section class="hero-visual" role="img" aria-label="Photo of a professional in a white shirt and dark tie standing by an office window overlooking the city">
    <div class="hero-word">MARLOW</div>
  </section>
</body>
</html>
```